Lunaria Set Social Media Graphics

Focusing on the Lunaria Harmony Set product, create 6-7 individual social media graphics (square size). For the color scheme of the graphics, they should all be complementary with the Lunaria Harmony Set bottle colors.

Note: each graphic should have one of the pictures of the bottles (3 product bundle) on it and/or one of the images with a person on it (several pics attached)/only use stock photography that I provided.

Target Market(s)

women over 50 dealing with menopause

Industry/Entity Type

health and wellness

Requirements
Must have
• the pictures/images I provided

```html
<!DOCTYPE html>
<html lang="en">
<head>
<meta charset="utf-8">
<title>Lunaria Set Social Media Graphics</title>
<link href="https://fonts.googleapis.com/css2?family=Montserrat:wght@400;500;600;700;800&display=swap" rel="stylesheet">
<style>
  :root{
    --teal:#4b8a7d;
    --teal-soft:#e4efec;
    --teal-deep:#2f6a5f;
    --coral:#e05b67;
    --ink:#2e2e2e;
    --card:#f6f6f6;
    --stage:#e8e8e8;
  }
  *{box-sizing:border-box;margin:0;padding:0}
  html,body{width:1200px;height:883px;overflow:hidden}
  body{background:var(--stage);font-family:"Montserrat",sans-serif;color:var(--ink);position:relative}
  .post{position:absolute;background:var(--card);overflow:hidden;box-shadow:0 4px 12px rgba(0,0,0,.12)}
  .post svg.art{position:absolute;inset:0;width:100%;height:100%}
  .post--feature{left:40px;top:182px;width:520px;height:520px}
  .post--solution{left:600px;top:152px;width:280px;height:280px}
  .post--lifeback{left:900px;top:152px;width:280px;height:280px}
  .post--goodbye{left:600px;top:452px;width:280px;height:280px}
  .post--answer{left:900px;top:452px;width:280px;height:280px}

  .brand{position:absolute;display:flex;align-items:center;gap:4px;font-weight:600;color:var(--teal)}
  .brand__dot{border-radius:50%;background:var(--teal);display:block}
  .post--feature .brand{right:20px;top:20px;font-size:13px}
  .post--feature .brand__dot{width:12px;height:12px}
  .post .brand{font-size:8px}
  .post .brand__dot{width:8px;height:8px}
  .post--solution .brand,.post--goodbye .brand,.post--answer .brand{left:14px;top:18px}
  .post--lifeback .brand{left:12px;top:182px}

  .copy{position:absolute;text-transform:uppercase;line-height:1.15}
  .copy .lead{font-weight:700}
  .copy .head{font-weight:800;color:var(--teal)}
  .copy .small{font-weight:500}
  .copy .accent{color:var(--coral);font-weight:700}

  .post--feature .copy{left:0;right:0;top:400px;text-align:center}
  .post--feature .lead{font-size:12px;font-weight:600}
  .post--feature .head{font-size:22px;margin:4px 0 8px}
  .post--feature .small{font-size:11px}
  .post--feature .accent{font-size:11px;display:block;margin-top:3px}

  .post--solution .copy{left:12px;top:184px}
  .post--solution .lead{font-size:19px;color:var(--ink)}
  .post--solution .head{font-size:20px}
  .post--solution .small{font-size:9.5px;margin-top:6px;line-height:1.4}

  .post--lifeback .copy{left:0;right:0;top:213px;text-align:center}
  .post--lifeback .head{font-size:14px;line-height:1.3}
  .post--lifeback .dark{color:var(--ink)}
  .post--lifeback .small{font-size:9.5px;margin-top:4px}

  .post--goodbye .copy{left:12px;top:56px}
  .post--goodbye .lead{font-size:16px}
  .post--goodbye .head{font-size:16px}
  .post--goodbye .accent{font-size:8px;font-weight:500;margin-top:12px;line-height:1.35}
  .post--goodbye .tail{font-size:9.5px;font-weight:700;margin-top:10px}

  .post--answer .copy{left:0;right:0;top:212px;text-align:center}
  .post--answer .head{font-size:10px;line-height:1.45}
  .post--answer .dark{color:var(--ink)}
  .post--answer .accent{font-size:7px;font-weight:600;margin-top:6px;display:block}
</style>
</head>
<body>

<!-- Feature post: product bundle -->
<section class="post post--feature">
  <svg class="art" viewBox="0 0 100 100" preserveAspectRatio="none">
    <defs>
      <linearGradient id="bundleTone" x1="0" y1="0" x2="0" y2="1">
        <stop offset="0" stop-color="#2f6a5f"/><stop offset=".55" stop-color="#9fc2b9"/><stop offset="1" stop-color="#f2f2f2"/>
      </linearGradient>
    </defs>
    <circle cx="85" cy="88" r="32" fill="var(--teal-soft)"/>
    <circle cx="0" cy="0" r="13" fill="var(--teal)"/>
    <circle cx="40" cy="-5" r="14" fill="none" stroke="var(--coral)" stroke-width=".35"/>
    <circle cx="0" cy="100" r="15" fill="none" stroke="var(--coral)" stroke-width=".35"/>
    <ellipse cx="48" cy="38" rx="29" ry="32" fill="none" stroke="var(--coral)" stroke-width=".3"/>
    <ellipse cx="48" cy="39" rx="25" ry="29" fill="url(#bundleTone)" stroke="var(--coral)" stroke-width="1.4" role="img" aria-label="Product photo: the three Lunaria Harmony Set bottles"/>
    <g fill="none" stroke="var(--coral)" stroke-width=".45">
      <polyline points="83,28 87,25 91,28"/><polyline points="83,31 87,28 91,31"/>
      <polyline points="83,34 87,31 91,34"/><polyline points="83,37 87,34 91,37"/>
      <polyline points="83,40 87,37 91,40"/>
    </g>
    <g stroke="#e8a3a9" stroke-width=".5">
      <path d="M8 49l2 2M10 49l-2 2"/><path d="M88 54l2 2M90 54l-2 2"/>
    </g>
    <g fill="#e8a3a9"><circle cx="8" cy="24" r=".35"/><circle cx="10" cy="24" r=".35"/><circle cx="12" cy="24" r=".35"/><circle cx="14" cy="24" r=".35"/></g>
    <rect x="80" y="73" width="24" height="5" rx="2.5" fill="var(--teal)"/>
    <g fill="#fff"><circle cx="85" cy="75.5" r="1.3"/><circle cx="89.5" cy="75.5" r="1.3"/><circle cx="94" cy="75.5" r="1.3"/></g>
  </svg>
  <div class="brand"><span class="brand__dot"></span>Vitalis Care</div>
  <div class="copy">
    <div class="lead">Struggling with</div>
    <div class="head">Menopause symptoms?</div>
    <div class="small">The solution you've been</div>
    <span class="accent">waiting for!</span>
  </div>
</section>

<!-- Post: the menopause solution -->
<section class="post post--solution">
  <svg class="art" viewBox="0 0 100 100" preserveAspectRatio="none">
    <circle cx="0" cy="30" r="11" fill="var(--teal)"/>
    <circle cx="62" cy="102" r="13" fill="var(--teal)"/>
    <circle cx="40" cy="-6" r="12" fill="none" stroke="var(--coral)" stroke-width=".4"/>
    <circle cx="72" cy="30" r="38" fill="var(--coral)"/>
    <circle cx="73" cy="29" r="35" fill="#8a6f5e" role="img" aria-label="Photo: smiling woman standing at a kitchen counter with the Lunaria Harmony Set"/>
    <g fill="none" stroke="var(--coral)" stroke-width=".5">
      <polyline points="24,25 27,22 30,25"/><polyline points="24,28 27,25 30,28"/>
      <polyline points="24,31 27,28 30,31"/><polyline points="24,34 27,31 30,34"/>
    </g>
    <g stroke="#e8a3a9" stroke-width=".6"><path d="M24 49l2 2M26 49l-2 2"/><path d="M32 64l2 2M34 64l-2 2"/></g>
    <rect x="78" y="87" width="25" height="5" rx="2.5" fill="var(--teal)"/>
    <g fill="#fff"><circle cx="83" cy="89.5" r="1.2"/><circle cx="87.5" cy="89.5" r="1.2"/><circle cx="92" cy="89.5" r="1.2"/></g>
  </svg>
  <div class="brand"><span class="brand__dot"></span>Vitalis Care</div>
  <div class="copy">
    <div class="lead">The</div>
    <div class="head">Menopause</div>
    <div class="small">Solution you've been<br><span class="accent">waiting</span> for is here!</div>
  </div>
</section>

<!-- Post: get your life back -->
<section class="post post--lifeback">
  <svg class="art" viewBox="0 0 100 100" preserveAspectRatio="none">
    <circle cx="104" cy="26" r="11" fill="var(--teal)"/>
    <circle cx="0" cy="100" r="12" fill="var(--teal)"/>
    <circle cx="0" cy="0" r="12" fill="none" stroke="var(--coral)" stroke-width=".4"/>
    <path d="M18 0V40a32 32 0 0 0 64 0V0Z" fill="var(--coral)"/>
    <path d="M21 0V40a29 29 0 0 0 58 0V0Z" fill="#8c7a6a" role="img" aria-label="Photo: woman in a brown sweater holding a Lunaria Harmony Set bottle"/>
    <g fill="none" stroke="var(--coral)" stroke-width=".5">
      <polyline points="6,34 10,31 14,34"/><polyline points="6,37 10,34 14,37"/>
      <polyline points="6,40 10,37 14,40"/><polyline points="6,43 10,40 14,43"/>
    </g>
    <g stroke="#e8a3a9" stroke-width=".6"><path d="M89 6l2 2M91 6l-2 2"/><path d="M89 45l2 2M91 45l-2 2"/><path d="M89 90l2 2M91 90l-2 2"/></g>
    <rect x="79" y="65" width="25" height="5" rx="2.5" fill="var(--teal)"/>
    <g fill="#fff"><circle cx="84" cy="67.5" r="1.2"/><circle cx="88.5" cy="67.5" r="1.2"/><circle cx="93" cy="67.5" r="1.2"/></g>
  </svg>
  <div class="brand"><span class="brand__dot"></span>Vitalis Care</div>
  <div class="copy">
    <div class="head"><span class="dark">Menopausal or</span><br>Post-menopausal?</div>
    <div class="small">Get your <span class="accent">life back</span></div>
  </div>
</section>

<!-- Post: say goodbye -->
<section class="post post--goodbye">
  <svg class="art" viewBox="0 0 100 100" preserveAspectRatio="none">
    <circle cx="102" cy="0" r="16" fill="var(--teal)"/>
    <circle cx="0" cy="69" r="18" fill="var(--teal)"/>
    <circle cx="50" cy="-6" r="12" fill="none" stroke="var(--coral)" stroke-width=".4"/>
    <path d="M44 100V36a28 28 0 0 1 56 0V100Z" fill="var(--coral)" transform="translate(2 0)"/>
    <path d="M46 100V38a26 26 0 0 1 52 0V100Z" fill="#b9a89a" role="img" aria-label="Photo: smiling woman with curly grey hair in a floral blouse"/>
    <g fill="none" stroke="var(--coral)" stroke-width=".5">
      <polyline points="28,63 31,60 34,63"/><polyline points="28,66 31,63 34,66"/>
      <polyline points="28,69 31,66 34,69"/><polyline points="28,72 31,69 34,72"/>
    </g>
    <g stroke="#e8a3a9" stroke-width=".6"><path d="M33 53l2 2M35 53l-2 2"/><path d="M22 78l2 2M24 78l-2 2"/><path d="M28 85l2 2M30 85l-2 2"/><path d="M86 21l2 2M88 21l-2 2"/></g>
    <rect x="-4" y="93" width="26" height="5" rx="2.5" fill="var(--teal)"/>
    <g fill="#fff"><circle cx="5" cy="95.5" r="1.2"/><circle cx="10.5" cy="95.5" r="1.2"/><circle cx="16" cy="95.5" r="1.2"/></g>
  </svg>
  <div class="brand"><span class="brand__dot"></span>Vitalis Care</div>
  <div class="copy">
    <div class="lead">Say</div>
    <div class="head">Goodbye to</div>
    <div class="accent">Hot flashes<br>and night sweats</div>
    <div class="tail">For good!</div>
  </div>
</section>

<!-- Post: we've got the answer -->
<section class="post post--answer">
  <svg class="art" viewBox="0 0 100 100" preserveAspectRatio="none">
    <circle cx="100" cy="0" r="11" fill="var(--teal)"/>
    <circle cx="88" cy="42" r="30" fill="var(--teal-soft)"/>
    <circle cx="0" cy="100" r="14" fill="none" stroke="var(--coral)" stroke-width=".4"/>
    <circle cx="104" cy="30" r="10" fill="none" stroke="var(--coral)" stroke-width=".4"/>
    <path d="M50 4c14 0 22 10 21 20c10 1 16 11 14 22c-2 12-14 18-35 18s-33-6-35-18c-2-11 4-21 14-22c-1-10 7-20 21-20Z" fill="var(--coral)"/>
    <path d="M50 6.5c12.5 0 19.5 9 18.5 19c9.5 .5 14.5 10 12.7 20c-1.8 10.8-12.7 16-31.2 16s-29.4-5.2-31.2-16c-1.8-10 3.2-19.5 12.7-20c-1-10 6-19 18.5-19Z" fill="#7d7b79" role="img" aria-label="Photo: smiling woman with short grey hair in a dark blazer"/>
    <g fill="none" stroke="var(--coral)" stroke-width=".5">
      <polyline points="6,32 10,29 14,32"/><polyline points="6,35 10,32 14,35"/>
      <polyline points="6,38 10,35 14,38"/><polyline points="6,41 10,38 14,41"/>
    </g>
    <g stroke="#e8a3a9" stroke-width=".6"><path d="M15 61l2 2M17 61l-2 2"/><path d="M88 13l2 2M90 13l-2 2"/><path d="M89 55l2 2M91 55l-2 2"/></g>
    <rect x="79" y="69" width="25" height="5" rx="2.5" fill="var(--teal)"/>
    <g fill="#fff"><circle cx="84" cy="71.5" r="1.2"/><circle cx="88.5" cy="71.5" r="1.2"/><circle cx="93" cy="71.5" r="1.2"/></g>
  </svg>
  <div class="brand"><span class="brand__dot"></span>Vitalis Care</div>
  <div class="copy">
    <div class="head">Menopause,<br><span class="dark">Post-menopause,</span><br>or hysterectomy symptoms?</div>
    <span class="accent">We've got the answer!</span>
  </div>
</section>

</body>
</html>
```